Quorra Pharmacy Brokers Business Card

Hi Desmond - thank you for the Logo - I'm very happy with it.

Can you please design a business card for me using the logo we've decided on.
Updates

Phone Number is (03) 8247 3106 Fax Number is (03) 8247 3107 Please update on the business card Thank you

Industry/Entity Type

Business

```html
<!DOCTYPE html>
<html lang="en">
<head>
<meta charset="utf-8">
<title>Quorra Pharmacy Brokers – Business Card</title>
<link rel="stylesheet" href="https://fonts.googleapis.com/css2?family=Open+Sans:wght@400;700&display=swap">
<style>
  :root {
    --backdrop: #d9d6d1;
    --card: #efefef;
    --ink: #1c1c1c;
    --ink-soft: #2e2e2e;
    --accent: #e8891c;
  }
  * { box-sizing: border-box; margin: 0; padding: 0; }
  html, body {
    width: 1200px; height: 900px; overflow: hidden;
    background: var(--backdrop);
    font-family: "Open Sans", Arial, sans-serif;
    color: var(--ink);
  }
  .canvas {
    position: relative; width: 1200px; height: 900px;
  }
  .card {
    position: absolute; left: 280px; width: 640px; height: 366px;
    background: var(--card);
    box-shadow: 0 6px 18px rgba(0,0,0,.18);
  }
  .card--front { top: 42px; }
  .card--back  { top: 492px; }

  .brand {
    position: absolute;
    font-weight: 700; color: var(--ink);
    letter-spacing: -0.5px; white-space: nowrap;
  }
  .card--front .brand { left: 0; right: 0; top: 160px; text-align: center; font-size: 34px; }
  .card--back  .brand { left: 96px; top: 44px; font-size: 28px; }

  .holder {
    position: absolute; left: 206px; top: 96px;
    font-size: 13px; color: var(--ink-soft);
  }
  .address {
    position: absolute; left: 40px; top: 190px;
    font-size: 15px; line-height: 20px; color: var(--ink);
  }
  .contacts {
    position: absolute; left: 352px; top: 200px; width: 250px;
    list-style: none; font-size: 17px; line-height: 21px;
  }
  .contacts li { display: flex; align-items: center; gap: 6px; }
  .contacts svg { width: 13px; height: 13px; flex: none; }
  .contacts .email {
    border-bottom: 2px solid var(--accent); padding-bottom: 3px;
  }
  .web {
    position: absolute; left: 352px; top: 294px;
    font-size: 16px; color: var(--ink);
  }
</style>
</head>
<body>
<main class="canvas">
  <section class="card card--front" aria-label="Card front">
    <div class="brand">Quorra Pharmacy Brokers</div>
  </section>

  <section class="card card--back" aria-label="Card back">
    <div class="brand">Quorra Pharmacy Brokers</div>
    <p class="holder">Martin Hale | Director</p>
    <p class="address">Shop 4, 27 - 31 Larkfield Road<br>LARKFIELD VICTORIA&nbsp;&nbsp;3190</p>
    <ul class="contacts">
      <li>
        <svg viewBox="0 0 14 14" aria-label="Mobile"><rect x="3" y="0.5" width="8" height="13" rx="1.5" fill="none" stroke="var(--accent)" stroke-width="1.6"/><rect x="5.5" y="10.5" width="3" height="1.4" fill="var(--accent)"/></svg>
        0412 738 265
      </li>
      <li>
        <svg viewBox="0 0 14 14" aria-label="Phone"><rect width="14" height="14" rx="2" fill="var(--accent)"/><path d="M4 3.5c0 4 2.5 6.5 6.5 6.5l.5-1.8-2-1-1 1c-1-.5-1.8-1.3-2.2-2.2l1-1-1-2z" fill="#fff"/></svg>
        (03) 8247 3106
      </li>
      <li>
        <svg viewBox="0 0 14 14" aria-label="Fax"><rect x="3.5" y="1" width="7" height="4" fill="var(--accent)"/><rect x="1" y="5" width="12" height="6" rx="1" fill="var(--accent)"/><rect x="3.5" y="9" width="7" height="4" fill="#fff" stroke="var(--accent)" stroke-width="1.2"/></svg>
        (03) 8247 3107
      </li>
      <li class="email">
        <svg viewBox="0 0 14 14" aria-label="Email"><rect x="0.5" y="3" width="13" height="9" fill="var(--accent)"/><path d="M1 3.5l6 4.5 6-4.5" fill="none" stroke="#fff" stroke-width="1.2"/></svg>
        mhale@quorrapb.com.au
      </li>
    </ul>
    <p class="web">www.quorrapb.com.au</p>
  </section>
</main>
</body>
</html>
```